Sports hypnotherapist needs electronic letterhead design

Need a simple but classy design for a letterhead that looks good when printed. Its for a hypnotherapist who specialises in elite sport. Should have my company name and address and website details on it. I specialise in footballers.
Should look good electronically and when printed.
Include all contact details as shown in the must haves.

Target Market(s)

Sports people, elite sport.

Industry/Entity Type

Hypnotherapy

Font styles to use
Sans Serif

Colors

Designer to choose colors to be used in the design.

Requirements
Must have
• NEEDS TO BE DESIGNED IN MS WORD
• Logo +
• Tidewell Focus Hypnotherapists
• 27 Harrowmere Close
• Bracknell
• RG19 4TX
• Tel: 07700 900461
• E: tidewellfocuscoaching@quorvex.co.uk
• www: http://www.tidewell-focus.co.uk.
• Dorian Lacey
• Clinical hypnotherapist, hypnoanalyst, mental resilience coach, MSc, Dip PHH
Nice to have
• A watermark?
• Plenty of space for the A4 letter
• Prints well.
Should not have
• Too much clutter.
• Too much colour that will be costly to print.

```html
<!DOCTYPE html>
<html lang="en">
<head>
<meta charset="utf-8">
<title>Tidewell Focus Letterhead</title>
<link href="https://fonts.googleapis.com/css2?family=Open+Sans:wght@400;600;700&family=Tinos:wght@400;700&display=swap" rel="stylesheet">
<style>
  :root {
    --backdrop: #e6e6e6;
    --paper: #f9f9f9;
    --accent: #25b8e8;
    --ink: #111111;
    --ink-soft: #333333;
    --footer-ink: #555555;
    --watermark-grey: #dcdcdc;
    --watermark-blue: #e2f3fa;
  }
  * { box-sizing: border-box; margin: 0; padding: 0; }
  html, body {
    width: 1200px; height: 1200px; overflow: hidden;
    background: var(--backdrop);
  }
  .letterhead {
    position: absolute; left: 227px; top: 20px;
    width: 746px; height: 1160px;
    background: var(--paper);
    overflow: hidden;
    font-family: "Open Sans", Arial, sans-serif;
  }
  .edge-band { position: absolute; left: 0; top: 0; width: 30px; height: 265px; }
  .watermark {
    position: absolute; left: 285px; top: 320px;
    width: 470px; height: 720px;
    border-radius: 120px 120px 40px 40px;
    background: linear-gradient(100deg, var(--watermark-grey) 0%, var(--watermark-grey) 45%, var(--watermark-blue) 60%, rgba(226,243,250,0) 100%);
    opacity: .8;
  }
  .brand {
    position: absolute; left: 28px; top: 62px;
    display: flex; align-items: center; gap: 12px;
  }
  .brand-dot { width: 30px; height: 30px; border-radius: 50%; background: var(--accent); }
  .brand-name { font-weight: 700; font-size: 36px; color: var(--ink); letter-spacing: -0.5px; }
  .practitioner {
    position: absolute; right: 51px; top: 79px;
    text-align: right; font-size: 14px; color: var(--ink); line-height: 19px;
  }
  .practitioner-name { font-size: 14px; margin-bottom: 12px; font-weight: 600; }
  .practitioner-name .first { color: var(--accent); font-weight: 400; }
  .letter {
    position: absolute; left: 57px; right: 55px; top: 0;
    font-family: "Tinos", "Times New Roman", serif;
    font-size: 15.4px; line-height: 19px; color: var(--ink);
  }
  .letter p { position: absolute; left: 0; right: 0; }
  .letter .justified { text-align: justify; }
  .issue-date { top: 343px; }
  .recipient { top: 419px; }
  .reference { top: 532px; font-weight: 700; }
  .salutation { top: 607px; }
  .para-one { top: 645px; }
  .para-two { top: 719px; }
  .para-three { top: 794px; }
  .closing { top: 870px; }
  .contact {
    position: absolute; top: 1064px;
    display: flex; flex-direction: column; align-items: center;
    font-size: 14px; line-height: 19px; color: var(--footer-ink); text-align: center;
  }
  .contact svg { width: 38px; height: 38px; margin-bottom: 4px; }
  .contact-phone { left: 111px; transform: translateX(-50%); }
  .contact-web { left: 346px; transform: translateX(-50%); }
  .contact-address { left: 587px; transform: translateX(-50%); text-align: left; }
</style>
</head>
<body>
<div class="letterhead">
  <svg class="edge-band" viewBox="0 0 30 265" aria-hidden="true">
    <path d="M0 0 H30 V205 C30 235 12 250 0 265 Z" fill="var(--accent)"/>
    <path d="M0 250 C14 240 24 222 30 200 V215 C24 238 12 252 0 262 Z" fill="#ffffff"/>
  </svg>

  <div class="watermark" role="img" aria-label="Faint watermark of a standing coach figure and a running athlete"></div>

  <div class="brand">
    <span class="brand-dot"></span>
    <span class="brand-name">Tidewell Focus</span>
  </div>

  <div class="practitioner">
    <p class="practitioner-name"><span class="first">DORIAN</span> LACEY</p>
    <p>Clinical hypnotherapist, hypnoanalyst</p>
    <p>mental resilience coach, MSc, Dip PHH</p>
  </div>

  <div class="letter">
    <p class="issue-date">Issuing date: May 5, 2012</p>
    <p class="recipient">Name of employee: Mr. xyz<br>Address of employee<br>address line 2</p>
    <p class="reference">Ref: Promotion as an Assistant secretary</p>
    <p class="salutation">Dear Mr. xyz,</p>
    <p class="para-one justified">I have the pleasure to inform you that you have been promoted as assistant secretary in the share department of the company. You are required to take charge of the new assignment on 15<sup style="font-size:9px">th</sup> May, 2012. Please accept my hearty congratulations on your promotion.</p>
    <p class="para-two justified">Your salary scale in the promoted cadre will be Tk. 16,000 and from 15th may, your basic salary will be fixed at Tk. 12,000 in the said scale. You will be entitled to all other allowances as applicable to the staff-II of the company. Other services conditions remain unchanged.</p>
    <p class="para-three">Please acknowledge receipt of this letter.</p>
    <p class="closing">Yours sincerely,</p>
  </div>

  <div class="contact contact-phone">
    <svg viewBox="0 0 38 38" aria-hidden="true">
      <circle cx="19" cy="19" r="19" fill="var(--accent)"/>
      <path d="M13 11 C12 11 11 12 11 13.5 C11.5 20 18 26.5 24.5 27 C26 27 27 26 27 25 L27 23 L23.5 21.5 L21.5 23.3 C19 22 16 19 14.7 16.5 L16.5 14.5 L15 11 Z" fill="#ffffff"/>
    </svg>
    <span style="margin-top:6px">07700 900461</span>
  </div>

  <div class="contact contact-web">
    <svg viewBox="0 0 38 38" aria-hidden="true">
      <circle cx="19" cy="19" r="19" fill="var(--accent)"/>
      <circle cx="19" cy="19" r="9" fill="none" stroke="#ffffff" stroke-width="2"/>
      <path d="M10 19 H28 M19 10 C15 14 15 24 19 28 M19 10 C23 14 23 24 19 28" fill="none" stroke="#ffffff" stroke-width="1.6"/>
    </svg>
    <span>tidewellfocuscoaching@quorvex.co.uk</span>
    <span>www.tidewell-focus.co.uk</span>
  </div>

  <div class="contact contact-address">
    <svg viewBox="0 0 38 38" aria-hidden="true" style="align-self:center">
      <circle cx="19" cy="19" r="19" fill="var(--accent)"/>
      <path d="M19 9 C15 9 12.5 12 12.5 15.5 C12.5 20 19 28 19 28 C19 28 25.5 20 25.5 15.5 C25.5 12 23 9 19 9 Z" fill="#ffffff"/>
      <circle cx="19" cy="15.5" r="2.6" fill="var(--accent)"/>
    </svg>
    <span style="margin-top:2px">CLINIC 9 Larkwell Street,</span>
    <span>Ashbury, Qld 4390</span>
  </div>
</div>
</body>
</html>
```